The Copper Nine: Book 2 of the Hollow Meridian trilogy

profile of a girl's head, and it should look like her, but with an image inside of it like the symbol of The Copper Nine, attached. Outside the profile should have a similar color scheme as the sky of the first cover

Target Market(s)

Young Adult (females primarily)

Industry/Entity Type

Entertainment

Other font styles liked:
• the one used on the first cover

Colors
33a6d7
876aae
eda3c7

Requirements
Must have
• It needs to look continuous with the first book in the series -- at least something connecting the two, same font, ideally same background.

```html
<!DOCTYPE html>
<html lang="en">
<head>
<meta charset="UTF-8">
<title>Copper Nine — Book Cover</title>
<link rel="stylesheet" href="https://fonts.googleapis.com/css2?family=Cinzel:wght@400;500&display=swap">
<style>
  :root {
    --page: #ffffff;
    --teal: #2f7f8c;
    --yellow: #f3e83a;
    --amber: #f6a11f;
    --orange: #ee5a12;
    --red: #d81a10;
    --deep-red: #8e0d08;
    --shadow: #1e1a1a;
    --title: #ffffff;
  }
  html, body {
    margin: 0;
    padding: 0;
    width: 1200px;
    height: 1200px;
    overflow: hidden;
    background: var(--page);
  }
  .canvas {
    position: relative;
    width: 1200px;
    height: 1200px;
    background: var(--page);
  }
  .cover {
    position: absolute;
    left: 240px;
    top: 60px;
    width: 720px;
    height: 1080px;
    overflow: hidden;
    background:
      linear-gradient(135deg,
        var(--teal) 0%,
        #b7c9a8 12%,
        var(--yellow) 30%,
        var(--amber) 45%,
        var(--orange) 60%,
        var(--red) 78%,
        var(--deep-red) 100%);
  }
  .cover__streaks {
    position: absolute;
    inset: 0;
    background:
      repeating-linear-gradient(135deg,
        rgba(255,255,255,0.10) 0px,
        rgba(255,255,255,0.10) 2px,
        rgba(0,0,0,0.06) 3px,
        rgba(0,0,0,0.06) 6px,
        transparent 7px,
        transparent 11px);
    mix-blend-mode: overlay;
  }
  .cover__portrait {
    position: absolute;
    left: 0;
    top: 0;
    width: 720px;
    height: 1080px;
  }
  .cover__title {
    position: absolute;
    left: 0;
    right: 0;
    text-align: center;
    font-family: "Cinzel", "Times New Roman", serif;
    color: var(--title);
    text-shadow: 0 2px 6px rgba(60, 10, 0, 0.45);
    margin: 0;
    line-height: 1;
  }
  .cover__title-top {
    top: 612px;
    font-size: 100px;
    font-weight: 400;
    letter-spacing: -2px;
    padding-left: 20px;
  }
  .cover__title-main {
    top: 742px;
    font-size: 250px;
    font-weight: 500;
    letter-spacing: -8px;
  }
</style>
</head>
<body>
  <div class="canvas">
    <div class="cover">
      <svg class="cover__portrait" viewBox="0 0 720 1080" role="img" aria-label="Blurred red profile of a girl's head with a glowing yellow Copper Nine symbol inside it">
        <defs>
          <radialGradient id="head-glow" cx="0.5" cy="0.45" r="0.55">
            <stop offset="0" stop-color="#f7b53a" stop-opacity="0.95"/>
            <stop offset="0.45" stop-color="#d8261a" stop-opacity="0.9"/>
            <stop offset="1" stop-color="#c81810" stop-opacity="0"/>
          </radialGradient>
          <linearGradient id="shoulder-shade" x1="0" y1="0" x2="0" y2="1">
            <stop offset="0" stop-color="#b51510" stop-opacity="0"/>
            <stop offset="0.5" stop-color="#3a1412" stop-opacity="0.85"/>
            <stop offset="1" stop-color="#1e1a1a"/>
          </linearGradient>
        </defs>
        <ellipse cx="300" cy="320" rx="270" ry="330" fill="url(#head-glow)"/>
        <rect x="0" y="640" width="330" height="440" fill="url(#shoulder-shade)"/>
      </svg>
      <div class="cover__streaks"></div>
      <h1 class="cover__title cover__title-top">Copper</h1>
      <p class="cover__title cover__title-main">Nine</p>
    </div>
  </div>
</body>
</html>
```